Corvalen Capital Modern Business Card

We need a modern business card template designed for Corvalen Capital.
Corvalen Capital is a diversified global cryptocurrency investment fund.

The font under the logo: Hiragino Kaku Gothic Pro

Color Hexcode: Main colors white (ffffff) & teal (188383), we are open to adding #fcca46 as an accent

Need time to get feedback from my team and to make sure designers better understand the brief.

Target Market(s)

Accredited Investors, high net worth individuals and institutional investors

Industry/Entity Type

Investment

Contact Information for Business Card

Contact Information should contain
Name
main phone +1 720 555 0147
cell
email

Font styles to use
Sans Serif
Other font styles liked:
• Hiragino Kaku Gothic Pro

Requirements
Must have
• would like to have icons that identify the contact information
• include our website: www.corvalencapital.example
• include our Tagline: Diversified Crypto Investment Funds
Nice to have
• Would like to have a simple back side with the logo (without the words) and plenty of space

```html
<!DOCTYPE html>
<html lang="en">
<head>
<meta charset="utf-8">
<title>Corvalen Capital Business Card</title>
<link rel="stylesheet" href="https://fonts.googleapis.com/css2?family=Jost:wght@400;500&display=swap">
<style>
  :root {
    --teal: #1b9393;
    --teal-deep: #188383;
    --teal-soft: #7fc6c6;
    --teal-pale: #a9d8d8;
    --icon-bg: #8fcaca;
    --white: #ffffff;
    --backdrop: #eef0f0;
  }
  * { box-sizing: border-box; margin: 0; padding: 0; }
  html, body {
    width: 1200px; height: 1200px; overflow: hidden;
    background: var(--backdrop);
    font-family: "Jost", sans-serif;
  }
  .canvas { position: relative; width: 1200px; height: 1200px; }
  .card {
    position: absolute; left: 240px; width: 720px; height: 412px;
  }
  .card-front { top: 149px; background: var(--teal); color: var(--white); text-align: center; }
  .card-back  { top: 641px; background: var(--white); color: var(--teal); }

  .brand-lockup {
    position: absolute; top: 222px; left: 0; right: 0;
    display: flex; justify-content: center; align-items: center; gap: 14px;
  }
  .brand-mark { width: 20px; height: 20px; background: var(--white); }
  .brand-name { font-size: 30px; font-weight: 400; letter-spacing: 0.02em; text-transform: uppercase; }
  .tagline {
    position: absolute; top: 326px; left: 0; right: 0;
    font-size: 16px; letter-spacing: 0.36em; text-transform: uppercase; color: var(--teal-soft);
  }
  .website {
    position: absolute; top: 370px; left: 0; right: 0;
    font-size: 20px; color: var(--teal-pale);
  }

  .person { position: absolute; left: 56px; top: 40px; }
  .person-name { font-size: 22px; font-weight: 400; text-transform: uppercase; line-height: 1.1; }
  .person-title { font-size: 17px; line-height: 1.3; }

  .contact { position: absolute; left: 56px; top: 232px; font-size: 24px; line-height: 28.5px; list-style: none; }
  .contact li { display: flex; align-items: center; gap: 9px; }
  .contact .plain { padding-left: 0; }
  .icon { width: 17px; height: 17px; flex: none; }

  .mini-brand {
    position: absolute; right: 40px; bottom: 40px;
    display: flex; align-items: center; gap: 7px;
  }
  .mini-mark { width: 12px; height: 12px; background: var(--teal); }
  .mini-name { font-size: 12px; color: var(--teal); text-transform: uppercase; letter-spacing: 0.02em; }
</style>
</head>
<body>
<div class="canvas">
  <section class="card card-front">
    <div class="brand-lockup">
      <span class="brand-mark"></span>
      <span class="brand-name">Corvalen Capital</span>
    </div>
    <p class="tagline">Diversified Crypto Investment Funds</p>
    <p class="website">www.corvalencapital.example</p>
  </section>

  <section class="card card-back">
    <div class="person">
      <h1 class="person-name">Elias Marrow</h1>
      <p class="person-title">Chief Executive Officer</p>
    </div>
    <ul class="contact">
      <li class="plain">418 Harbor Lane</li>
      <li class="plain">Denver, CO</li>
      <li>
        <svg class="icon" viewBox="0 0 16 16" aria-hidden="true"><rect width="16" height="16" rx="3" fill="var(--icon-bg)"/><path d="M5 3.5l1.6 2.1-.9 1.1a6 6 0 0 0 3.6 3.6l1.1-.9 2.1 1.6-.9 1.6c-4 0-8-4-8-8z" fill="#fff"/></svg>
        <span>+1 720 555 0147</span>
      </li>
      <li>
        <svg class="icon" viewBox="0 0 16 16" aria-hidden="true"><rect width="16" height="16" rx="3" fill="var(--icon-bg)"/><rect x="5" y="3" width="6" height="10" rx="1" fill="#fff"/><rect x="6" y="4.2" width="4" height="6.5" fill="var(--icon-bg)"/></svg>
        <span>+1 720 555 0193</span>
      </li>
      <li>
        <svg class="icon" viewBox="0 0 16 16" aria-hidden="true"><rect width="16" height="16" rx="3" fill="var(--icon-bg)"/><rect x="3" y="5" width="10" height="7" fill="#fff"/><path d="M3 5l5 4 5-4" fill="none" stroke="var(--icon-bg)" stroke-width="1"/></svg>
        <span>emarrow@corvalencapital.example</span>
      </li>
    </ul>
    <div class="mini-brand">
      <span class="mini-mark"></span>
      <span class="mini-name">Corvalen Capital</span>
    </div>
  </section>
</div>
</body>
</html>
```